Aesthetic shopify website with functioning mobile version

I need a website that looks aesthetically pleasing using the pictures, logos, and product that I provide in the files. I also need to have an aesthetic easy to use mobile version as well.

Here is a list of things I want included in the website.
- Shipping rates are surfaced during checkout
- Discount codes can be applied in the cart
- A shopper can edit their cart’s content
- There is an option for order status tracking
- An email notification is sent to confirm a purchase

The domain is www.brandelio.com, so I am not sure how to go forward with having you convert it to that domain. I look forward to working with you!

```html
<!DOCTYPE html>
<html lang="en">
<head>
<meta charset="utf-8">
<title>Brandelio — Home</title>
<link rel="stylesheet" href="https://fonts.googleapis.com/css2?family=Fira+Sans:wght@500;600;700;800&family=Poppins:wght@500;600;700;800&family=Open+Sans:wght@400;600;700&display=swap">
<style>
:root{
  --brown:#75663f;
  --brown-dark:#5f5233;
  --ink:#1c1c1c;
  --text:#333;
  --muted:#666;
  --section-tint:#f4f0f0;
  --footer:#141414;
  --accent-red:#e4502d;
  --star:#f3b51b;
  --white:#fff;
}
*{box-sizing:border-box;margin:0;padding:0}
html,body{width:1200px;height:3930px;overflow:hidden}
body{position:relative;background:var(--white);font-family:"Open Sans",sans-serif;color:var(--text)}

/* header */
.site-header{position:absolute;left:0;top:0;width:1200px;height:82px;background:var(--white)}
.brand{position:absolute;left:133px;top:16px;font-family:"Poppins",sans-serif;font-weight:800;font-size:40px;color:var(--brown);letter-spacing:1px;line-height:1}
.main-nav{position:absolute;top:33px;left:0;width:1200px;font-size:14px;color:var(--ink)}
.main-nav a{position:absolute;color:inherit;text-decoration:none}
.main-nav .active{font-weight:700;text-decoration:underline;text-underline-offset:4px}
.cart{position:absolute;left:1026px;top:24px;width:40px;height:36px}

/* hero */
.hero{position:absolute;left:0;top:82px;width:1200px;height:620px;background:linear-gradient(90deg,#e7e4e3 0%,#eeebea 45%,#e9e5e3 100%);overflow:hidden}
.hero-photo{position:absolute;left:560px;top:0;width:640px;height:620px;background:radial-gradient(ellipse at 55% 45%,#d9a98f 0%,#b8553a 38%,#8c3a24 60%,rgba(233,229,227,0) 78%)}
.hero-copy{position:absolute;left:130px;top:168px;width:400px;text-align:center;font-family:"Fira Sans",sans-serif}
.hero-kicker{font-size:30px;font-weight:700;color:#3a3a3a;letter-spacing:1px}
.hero-title{font-size:68px;font-weight:800;color:#3a3a3a;letter-spacing:2px;line-height:1.05;margin-top:4px}
.hero-sub{font-size:21px;font-weight:600;color:var(--brown);line-height:30px;margin-top:18px;letter-spacing:.5px}
.btn{display:inline-block;background:var(--brown);color:var(--white);font-weight:600;text-decoration:none;text-align:center}
.hero-btn{position:absolute;left:249px;top:378px;width:159px;height:48px;line-height:48px;font-family:"Fira Sans",sans-serif;font-size:19px}
.hero-band{position:absolute;left:0;top:690px;width:1200px;height:22px;background:var(--brown)}

/* feature */
.feature-photo{position:absolute;left:0;top:829px;width:695px;height:396px;background:linear-gradient(90deg,#f3f1f0 0%,#ddd 40%,#5b3d2f 62%,#c9b6a7 100%)}
.feature-copy{position:absolute;left:768px;top:912px;width:300px}
.feature-copy h2{font-family:"Poppins",sans-serif;font-size:25px;font-weight:700;color:var(--ink);line-height:32px;white-space:nowrap}
.feature-copy p{font-size:13.5px;line-height:20px;margin-top:22px;color:var(--text)}
.feature-copy .btn{margin-top:29px;width:112px;height:36px;line-height:36px;font-size:13.5px}

.banner-photo{position:absolute;left:0;top:1303px;width:1200px;height:525px;background:radial-gradient(ellipse at 58% 50%,#e8c3a3 0%,#c79368 30%,#6f6a5f 65%,#3c3f37 100%)}

/* section heads */
.section-title{position:absolute;left:0;width:1200px;text-align:center;font-family:"Poppins",sans-serif;font-weight:700;font-size:26px;color:var(--ink)}
.section-rule{position:absolute;left:577px;width:46px;height:2px;background:#a9a9a9}

/* reviews */
.review{position:absolute;top:1967px;width:256px}
.review p{font-size:13px;line-height:20px;color:var(--text)}
.review .rule{position:absolute;top:203px;width:32px;height:2px;background:var(--accent-red)}
.review .stars{position:absolute;top:220px;color:var(--star);font-size:17px;letter-spacing:1px}
.review .name{position:absolute;top:244px;font-size:12px;color:var(--text)}

/* products */
.products{position:absolute;left:0;top:2295px;width:1200px;height:640px;background:var(--section-tint)}
.product-media{position:absolute;left:132px;top:2437px;width:470px;height:435px;background:var(--white)}
.product-tube{position:absolute;left:135px;top:38px;width:200px;height:310px;background:linear-gradient(180deg,#2c2c2c,#151515)}
.product-info{position:absolute;left:645px;top:2430px;width:420px}
.product-info h3{font-family:"Poppins",sans-serif;font-size:19.5px;font-weight:700;color:var(--ink)}
.product-info .desc{font-size:13px;line-height:18px;margin-top:6px;width:370px}
.product-info h4{font-size:12px;font-weight:700;color:var(--ink);margin:30px 0 0 4px}
.ingredients{list-style:none;margin:20px 0 0 18px}
.ingredients li{position:relative;font-size:13px;line-height:18px;padding-left:14px;margin-bottom:17px;width:390px}
.ingredients li::before{content:"";position:absolute;left:0;top:5px;border-left:5px solid var(--ink);border-top:4px solid transparent;border-bottom:4px solid transparent}
.price{position:absolute;left:656px;top:2770px;font-family:"Poppins",sans-serif;font-size:24px;font-weight:600;color:var(--ink)}
.product-btn{position:absolute;left:656px;top:2836px;width:112px;height:36px;line-height:36px;font-size:13.5px}

/* blog */
.post{position:absolute;top:3089px;width:274px}
.post .thumb{height:264px}
.post h3{font-family:"Poppins",sans-serif;font-size:13.5px;font-weight:600;line-height:19px;color:var(--ink);margin:27px 0 0 2px;width:250px}
.post p{font-size:13px;line-height:17.5px;margin:16px 0 0 2px;width:265px}
.post .more{display:block;margin:22px 0 0 2px;font-size:11px;font-weight:700;color:var(--brown);text-decoration:underline}

/* footer */
.site-footer{position:absolute;left:0;top:3620px;width:1200px;height:310px;background:var(--footer);color:#ddd}
.site-footer h5{position:absolute;top:43px;font-family:"Poppins",sans-serif;font-size:16px;font-weight:600;color:var(--white)}
.footer-about{position:absolute;left:133px;top:85px;width:280px;font-size:13px;line-height:20px}
.footer-menu{position:absolute;left:498px;top:82px;list-style:none;font-size:13px;line-height:21px}
.footer-join{position:absolute;left:724px;top:82px;font-size:13px}
.signup{position:absolute;left:724px;top:117px;width:341px;height:48px;border:1px solid #bbb}
.signup span{position:absolute;left:18px;top:15px;font-size:12px;color:#ddd}
.signup .go{position:absolute;right:-1px;top:-1px;width:48px;height:48px;background:var(--brown)}
.socials{position:absolute;left:133px;top:250px}
.socials span{position:absolute;top:0;width:26px;height:26px;border-radius:50%}
.copyright{position:absolute;left:0;top:256px;width:1200px;text-align:center;font-size:12px;color:#ddd}
.pay{position:absolute;top:250px;width:46px;height:28px;border-radius:3px}
</style>
</head>
<body>

<header class="site-header">
  <div class="brand">BRANDELIO</div>
  <nav class="main-nav">
    <a class="active" style="left:575px">HOME</a>
    <a style="left:653px">ABOUT US</a>
    <a style="left:762px">PRODUCTS</a>
    <a style="left:873px">FAQ</a>
    <a style="left:933px">SUPPORT</a>
  </nav>
  <svg class="cart" viewBox="0 0 40 36" aria-label="Cart, 0 items">
    <path d="M2 5h6l5 18h19l4-13H11" fill="none" stroke="#1c1c1c" stroke-width="2.4" stroke-linejoin="round"/>
    <path d="M14 14h20M15 18h17" stroke="#1c1c1c" stroke-width="1.6"/>
    <circle cx="15" cy="30" r="3" fill="#1c1c1c"/><circle cx="29" cy="30" r="3" fill="#1c1c1c"/>
    <circle cx="33" cy="8" r="7" fill="#75663f"/>
    <text x="33" y="11.5" font-size="10" font-family="Open Sans,sans-serif" font-weight="700" fill="#fff" text-anchor="middle">0</text>
  </svg>
</header>

<section class="hero">
  <div class="hero-photo" role="img" aria-label="Portrait of a woman with long wavy copper hair"></div>
  <div class="hero-copy">
    <div class="hero-kicker">WELCOME TO</div>
    <div class="hero-title">BRANDELIO</div>
    <div class="hero-sub">LOREM IPSUM IS SIMPLY DUMMY<br>TEXT OF THE PRINTING</div>
  </div>
  <a class="btn hero-btn">SHOP NOW</a>
</section>
<div class="hero-band" role="img" aria-label="Decorative ribbon along the bottom of the hero"></div>

<div class="feature-photo" role="img" aria-label="Curl defining cream tube beside a woman with dark curly hair"></div>
<div class="feature-copy">
  <h2>CURL DEFINING CREAM</h2>
  <p>Sed ut perspiciatis unde omnis iste natus error sit voluptatem accusantium doloremque laud antium, totam rem aperiam, eaque ipsa quae ab illo inventore veritatis et quasi architecto beatae vitae dict.</p>
  <a class="btn">SHOP NOW</a>
</div>

<div class="banner-photo" role="img" aria-label="Smiling woman in a straw hat with wavy hair"></div>

<h2 class="section-title" style="top:1874px">REVIEWS</h2>
<div class="section-rule" style="top:1922px"></div>

<article class="review" style="left:133px">
  <p>At vero eos et accusamus et iusto odio dign issimos ducimus qui blanditiis praesentium voluptatum deleniti atque corrupti quos dolores et quas molestias excepturi sint occaecati cupiditate non provident, similique sunt in culpa qui officia deserunt mollitia animi, id est laborum et dolorum fuga. Et harum quidem rerum facilis.</p>
  <div class="rule"></div><div class="stars">★★★★★</div><div class="name">Richard</div>
</article>
<article class="review" style="left:476px">
  <p>Sed ut perspiciatis unde omnis iste natus error sit voluptatem accusantium doloremque laudantium, totam rem aperiam, eaque ipsa quae ab illo inventore veritatis et quasi architecto beatae vitae dicta sunt explicabo. Nemo enim ipsam voluptatem quia voluptas sit aspernatur aut odit aut fugit, sed quia consequuntur</p>
  <div class="rule"></div><div class="stars">★★★★★</div><div class="name">Richard</div>
</article>
<article class="review" style="left:815px;width:248px">
  <p>But I must explain to you how all this mistaken idea of denouncing pleasure and praising pain was born and I will give you a complete account of the system, and expound the actual teachings of the great explorer of the truth, the master-builder of human happiness. No one rejects, dislikes, or avoids pleasure</p>
  <div class="rule"></div><div class="stars">★★★★★</div><div class="name">Richard</div>
</article>

<section class="products"></section>
<h2 class="section-title" style="top:2337px">OUR PRODUCTS</h2>
<div class="section-rule" style="top:2386px"></div>
<div class="product-media">
  <div class="product-tube" role="img" aria-label="Black tube of curl defining cream"></div>
</div>
<div class="product-info">
  <h3>Curl Defining Cream</h3>
  <p class="desc">This amplifying cream defines and separates while adding volume, shine and texture. Retains curl and reduces frizz for a radiant, touchable finish.</p>
  <h4>KEY INGREDIENTS</h4>
  <ul class="ingredients">
    <li>Simmondsia Chinensis (Jojoba) Seed Oil - Deep penetrating oil that softens and conditions</li>
    <li>Helianthus Annuus (Sunflower) Extract - Naturally-derived UV protectant for hair to prevent color fading, while also conditioning hair and adding shine</li>
    <li>Polyquaternium-11 - Plant- derived polymer to add volume and help thicken hair</li>
  </ul>
</div>
<div class="price">$125.00</div>
<a class="btn product-btn">SHOP NOW</a>

<h2 class="section-title" style="top:2991px">LATEST BLOG</h2>
<div class="section-rule" style="top:3043px"></div>

<article class="post" style="left:133px">
  <div class="thumb" role="img" aria-label="Woman with long red wavy hair" style="background:linear-gradient(135deg,#d7b6a2,#8e3b22 60%,#5a2515)"></div>
  <h3>Lorem Ipsum is simply dummy text of the printing</h3>
  <p>Sed ut perspiciatis unde omnis iste natus error sit voluptatem accusantium dolore mque laudantium, totam rem aperiam, eaque ipsa quae ab illo inventor.</p>
  <a class="more">READ MORE</a>
</article>
<article class="post" style="left:463px">
  <div class="thumb" role="img" aria-label="Woman with dark voluminous curls" style="background:linear-gradient(135deg,#2a2523,#6a5548 55%,#1c1816)"></div>
  <h3>Lorem Ipsum is simply dummy text of the printing</h3>
  <p>Sed ut perspiciatis unde omnis iste natus error sit voluptatem accusantium dolore mque laudantium, totam rem aperiam, eaque ipsa quae ab illo inventor.</p>
  <a class="more">READ MORE</a>
</article>
<article class="post" style="left:797px">
  <div class="thumb" role="img" aria-label="Woman with brown curled hair and earrings" style="background:linear-gradient(135deg,#cdbba5,#8a5a3e 55%,#d8c6b3)"></div>
  <h3>Lorem Ipsum is simply dummy text of the printing</h3>
  <p>Sed ut perspiciatis unde omnis iste natus error sit voluptatem accusantium dolore mque laudantium, totam rem aperiam, eaque ipsa quae ab illo inventor.</p>
  <a class="more">READ MORE</a>
</article>

<footer class="site-footer">
  <h5 style="left:133px">ABOUT</h5>
  <p class="footer-about">Lorem Ipsum is simply dummy text of the printing and typesetting industry. veritatis et qai architecto beatae vitae dicta sunt explicabo. Nemo enim ipsam</p>
  <h5 style="left:498px">MENU</h5>
  <ul class="footer-menu"><li>Products</li><li>About US</li><li>FAQ</li><li>Support</li><li>Reviews</li></ul>
  <h5 style="left:724px">STAY CONNECTED</h5>
  <p class="footer-join">Join our mailing list to get updates</p>
  <div class="signup">
    <span>E mail address</span>
    <svg class="go" viewBox="0 0 48 48" aria-hidden="true"><path d="M21 17l7 7-7 7" fill="none" stroke="#fff" stroke-width="2.2"/></svg>
  </div>
  <div class="socials">
    <span style="left:0;background:#3b5bab"></span>
    <span style="left:35px;background:#2a9ad8"></span>
    <span style="left:70px;background:#7d6ab0"></span>
  </div>
  <p class="copyright">Copyright © 2021 All Rights Reserved</p>
  <span class="pay" style="left:864px;background:#1f3f8f"></span>
  <span class="pay" style="left:916px;background:#1a3fa0"></span>
  <span class="pay" style="left:968px;background:#333"></span>
  <span class="pay" style="left:1020px;background:#2b6fc4"></span>
</footer>

</body>
</html>
```